Lanterns Beyond the Gate Book Cover

Looking for an inspirational cover for a Christian book called Lanterns Beyond the Gate - Mending the Weariness of the Heart & Spirit. This book features the real life stories of Delphine Orvall, a woman on a mission to spread the word of God to homeless people. The finished book will be 6" X 9", but the final page count is not known at this time. The cover should exude goodness and hope. Was thinking that the 1st "t" in the word "gate" could be made to look like a cross to create a stronger connection to the aspect of Christianity.

```html
<!DOCTYPE html>
<html lang="en">
<head>
<meta charset="utf-8">
<title>Lanterns Beyond the Gate — Book Cover</title>
<link rel="stylesheet" href="https://fonts.googleapis.com/css2?family=Bebas+Neue&family=Barlow+Condensed:wght@600&display=swap">
<style>
  :root {
    --backdrop: #e7e7e7;
    --sky-teal: #3c7a96;
    --mist-green: #8db3a6;
    --glow-gold: #f6dc92;
    --ember-orange: #e2985a;
    --dusk-plum: #6b4a56;
    --night-band: #2c2634;
    --title-white: #f4f3f1;
    --author-ink: #15161a;
  }
  * { margin: 0; padding: 0; box-sizing: border-box; }
  html, body {
    width: 1200px;
    height: 800px;
    overflow: hidden;
    background: var(--backdrop);
  }
  .stage {
    position: relative;
    width: 1200px;
    height: 800px;
  }
  .book-cover {
    position: absolute;
    left: 408px;
    top: 93px;
    width: 397px;
    height: 607px;
    overflow: hidden;
    border-radius: 3px;
    background: var(--night-band);
  }
  .cover-art {
    position: absolute;
    inset: 0;
    background:
      radial-gradient(ellipse 120px 160px at 56% 42%, rgba(255,246,214,0.95), rgba(255,236,170,0) 100%),
      linear-gradient(180deg,
        var(--sky-teal) 0%,
        var(--mist-green) 22%,
        var(--glow-gold) 42%,
        var(--ember-orange) 64%,
        var(--dusk-plum) 82%,
        var(--night-band) 95%);
  }
  .title-block { font-weight: 400; }
  .author-name,
  .title {
    position: absolute;
    left: 0;
    width: 100%;
    text-align: center;
    font-family: "Bebas Neue", "Oswald", sans-serif;
    line-height: 1;
    white-space: nowrap;
  }
  .author-name {
    top: 6px;
    font-size: 26px;
    letter-spacing: 0.3px;
    color: var(--author-ink);
  }
  .title { color: var(--title-white); }
  .title-lead { top: 320px; font-size: 113px; }
  .title-joiner { top: 415px; font-size: 39px; }
  .title-main { top: 445px; font-size: 154px; letter-spacing: 4px; }
  .subtitle {
    position: absolute;
    top: 578px;
    left: 0;
    width: 100%;
    text-align: center;
    font-family: "Barlow Condensed", "Oswald", sans-serif;
    font-weight: 600;
    font-size: 13px;
    letter-spacing: 1.2px;
    line-height: 1;
    white-space: nowrap;
    color: var(--title-white);
  }
</style>
</head>
<body>
  <main class="stage">
    <article class="book-cover">
      <div class="cover-art" role="img" aria-label="Placeholder area for the cover illustration, shown as a teal-to-gold-to-plum sunrise gradient"></div>
      <p class="author-name">Delphine Orvall</p>
      <h1 class="title-block">
        <span class="title title-lead">LANTERNS</span>
        <span class="title title-joiner">BEYOND THE</span>
        <span class="title title-main">GATE</span>
      </h1>
      <p class="subtitle">MENDING THE WEARINESS OF THE HEART &amp; SPIRIT</p>
    </article>
  </main>
</body>
</html>
```